Wrenfield food and drinks menu

Tamarind on Vellory is a vegan restaurant in NYC. It's food menu is given to guests on a casual clipboard, on regular sized 8.5 x 11 sheets of paper.

The assignment is to create a drinks menu to make the cocktail, wine and beer offerings more prominent. The drinks menu should be half the size of the regular menu so it sits smaller on top of the 8.5 x 11 sheet of paper. Other requirements:

-Please refer to the website design for inspiration and style guide
wrenfieldeats.com
-brand assets, the logo for Tamarind on Vellory and color treatments are here
https://www.filecrate.example/sh/8kqpwz2lmtdfa/QXvbnPzr4T
- if there is too much copy the drinks menu can be laid out on a 8.5 x 11 sheet of paper that opens like a book horizontally, with a front cover, then the inside left and right panels and back panel can have text.

The drinks menu should be organized by:

Organic Cocktails
Wines by the glass (white, red, rose)
Sparkling
Beer
Non alcoholic

List of drinks are enclosed

Industry/Entity Type

Restaurant

Requirements
Must have
• Tamarind on Vellory logo, and all the drink items listed in the attached menu.
Use fonts that are in the brand asset dropbox.
Should not have
• Lots of color. This will most likely not be printed in color.

```html
<!DOCTYPE html>
<html lang="en">
<head>
<meta charset="utf-8">
<title>Wrenfield food and drinks menu</title>
<link rel="stylesheet" href="https://fonts.googleapis.com/css2?family=Open+Sans:ital,wght@0,400;0,600;0,700;1,400;1,700&display=swap">
<style>
:root{
  --paper:#ffffff;
  --ink:#1f1f1f;
  --rule:#8a8a8a;
  --brand:#555555;
}
*{margin:0;padding:0;box-sizing:border-box}
html,body{width:1200px;height:1000px;overflow:hidden;background:var(--paper)}
body{font-family:"Open Sans",Arial,sans-serif;color:var(--ink);font-size:12.5px;line-height:15.5px;position:relative}
.column{position:absolute;top:0}
.column--left{left:249px;width:322px;letter-spacing:-.3px}
.column--right{left:625px;width:330px;letter-spacing:-.3px}
.section-title{font-size:15px;font-weight:400;letter-spacing:.2px;line-height:20px}
.section-title--center{text-align:center}
.drink{margin-bottom:15.5px}
.drink b{font-weight:700}
.drink i{font-style:italic}
.price{margin-left:12px}
.divider{width:115px;height:1px;background:var(--rule);margin:0 auto}
.wine-group{font-weight:700;font-style:italic;font-size:12.5px;line-height:15.5px}
.brandmark{position:absolute;left:676px;top:848px;width:212px;text-align:center;color:var(--brand);font-weight:400}
.brandmark__name{font-size:34px;line-height:36px;letter-spacing:1px}
.brandmark__place{font-size:15px;line-height:18px;letter-spacing:3px}
</style>
</head>
<body>

<section class="column column--left">
  <h2 class="section-title section-title--center" style="margin-top:24px;margin-bottom:12px">organic seasonal cocktails</h2>
  <p class="drink"><b>atalanta</b> - cinnamon infused vodka, pumpkin spice, apple juice, demerara sugar rim, over ice<span class="price">13</span></p>
  <p class="drink"><b>jaguar ride</b> - jalapeno tequila, sriracha bitters. fresh lemon/lime juice, orange liqueur, salt rim, up<span class="price">13</span></p>
  <p class="drink"><b>mojito “of the moment”</b> <i>(ask your bartender or server for today’s offering)</i><span class="price">12</span></p>
  <p class="drink"><b>châtelet</b> - vale gin, jasmine liqueur, splash of absinthe, lemon juice, up over sugar cube<span class="price">13</span></p>
  <p class="drink"><b>dale hollow</b> - harrow’s creek whiskey, housemade ginger syrup, muddled mint, sparkling water, over ice<span class="price">12</span></p>
  <p class="drink"><b>bloody wrenfield</b> - with vale vodka &nbsp;11/ with premium house infused jalapeno vodka<span class="price">12</span></p>
  <p class="drink"><b>classic g&amp;t</b> - vale gin, premium fenwick tonic, lime wheel, over ice<span class="price">11</span></p>
  <p class="drink" style="margin-bottom:26px"><b>house made seasonal sangria</b><span class="price">11</span></p>
  <div class="divider"></div>
  <h2 class="section-title section-title--center" style="margin-top:20px;margin-bottom:14px">beer</h2>
  <p class="drink">hollenau pilsner, germany (12oz bottle) 6</p>
  <p class="drink">abner crowe cider, united kingdom (12oz bottle)<br>*gluten free 6</p>
  <p class="drink">tamsin’s ipa, vermont (12oz bottle)&nbsp; 7</p>
  <p class="drink" style="margin-bottom:30px">ninefold bright tide, brooklyn (16oz can)&nbsp; 7</p>
  <div class="divider"></div>
  <h2 class="section-title" style="margin-top:27px;margin-bottom:12px">soft drinks and such</h2>
  <p class="drink">millbrook sparkling water &nbsp;(liter bottle)<span class="price">7</span></p>
  <p class="drink">grapefruit/cranberry juice<span class="price">4</span></p>
  <p class="drink">pomegranate/bilberry juice<span class="price">4.5</span></p>
  <p class="drink">jade cola / osric’s root beer<span class="price">3.5</span></p>
  <p class="drink">harlowe sparkling elderflower lemonade<span class="price">4</span></p>
  <p class="drink">house brewed fresh ginger ale<span class="price">5</span></p>
  <p class="drink">potted loose tea - assam black, sencha green.<br>peppermint, lavendar, chamomile, mixed berry<span class="price">4</span></p>
  <p class="drink">single espresso&nbsp; 3 / double espresso 4.5 /<br>americano&nbsp; 3.5 / cappucino&nbsp; 5</p>
</section>

<section class="column column--right">
  <h2 class="section-title section-title--center" style="margin-top:25px;margin-bottom:17px;margin-left:-10px">wine by the glass</h2>
  <p class="wine-group" style="margin-bottom:5px">white</p>
  <p class="drink">sauvignon blanc, the green cask, sonoma, california,<br>2012&nbsp;&nbsp; 9/36</p>
  <p class="drink">grillo, casa vellini, sicily, italy, 2012<span class="price">10/40</span></p>
  <p class="drink">verdejo, sierra moral, la mancha, spain, 2012<span class="price">10/40</span></p>
  <p class="drink">white blend (chard/sauv blanc/semillion), cedar slope, israel, 2011 <i>(kosher)</i><span class="price">10/0</span></p>
  <p class="drink">chardonnay, heron bend, lodi, california,<br>2011&nbsp;&nbsp;&nbsp; 11/44</p>
  <p class="drink" style="margin-bottom:31px">clairette/roussanne/marsanne/grenache blanc,<br>cotes du rhone, france, 2012<span class="price">12/48</span></p>
  <p class="wine-group" style="margin-bottom:5px">red</p>
  <p class="drink">red blend (bordeaux/rhone style), the green cask,<br>sonoma, california, 2009<span class="price">9/36</span></p>
  <p class="drink">cab sauv/petit verdot, shefer, israel, 2010<span class="price">10/40</span></p>
  <p class="drink">tempranillo/syrah, soil 4.0, la mancha, spain, 2010<span class="price">10/40</span></p>
  <p class="drink">malbec, los alerces, cafayette valley, argentina,<br>2012&nbsp;&nbsp;&nbsp; 11/44</p>
  <p class="drink">zinfandel, quaranta, sonoma, california, 2011&nbsp; 12/48</p>
  <p class="drink" style="margin-bottom:31px">pinot noir, valdemora, leyda valley, chile, 2012&nbsp; 13/52</p>
  <p class="wine-group" style="margin-bottom:5px">rose</p>
  <p class="drink" style="margin-bottom:31px">malbec/carignan, shefer, binyamina, israel, 2010,<br>(kosher)&nbsp; 11/44</p>
  <p class="wine-group" style="margin-bottom:1px">sparkling</p>
  <p class="drink">la brina prosecco di valdobbiandene, brut DOC, “ponente”,<br>italy&nbsp; 10/45</p>
  <p class="drink">castellfort, cava, brut nature, reserva, penedes, spain&nbsp; 60</p>
</section>

<div class="brandmark" role="img" aria-label="Tamarind on Vellory">
  <div class="brandmark__name">TAMARIND</div>
  <div class="brandmark__place">on Vellory</div>
</div>

</body>
</html>
```